Environmental Plastics Infographic on Marine Debris

We need a series of infographics that can be used individually or as a combined presentation. We'd like the combined piece to include an introduction and conclusion along with 4-5 infographics. Each infographic (information unit) should also work as a standalone. We are trying to help people visualize size proportions and ratios to put the plastics marine debris problem in perspective. Our key point is concerning polystyrene foam which represents 35 tons. We are looking for something creative to help people understand what the problem represents in terms they are familiar with.

To view our typical company design/style please see our website at www.harbenfoamworks.org. Our primary RGB colors are: (187,140,9); (94,47,29); (94,138,164); and (164,167,15). Secondary RGB colors are (249,162,28) and (218,210,208). Our title/header font is DIN Next LT Pro and our copy font is Calibri 10.5 pt. We can deviate from the font specification if beneficial and welcome interesting text treatments and typography.

Need extra days to review

Target Market(s)

international brand manufacturers (brenloch, tavix), US legislators & government agencies

Font styles to use
Sans Serif

Requirements
Must have
• Sufficient white space. Easy to grasp message concept with visual components.

```html
<!DOCTYPE html>
<html lang="en">
<head>
<meta charset="utf-8">
<title>Will Polystyrene Bans Improve Ocean Health</title>
<link href="https://fonts.googleapis.com/css2?family=Passion+One:wght@400;700&family=Open+Sans:wght@400;600;700&family=Libre+Baskerville:wght@700&display=swap" rel="stylesheet">
<style>
:root{
  --gold:#bb8c09;
  --brown:#5e2f1d;
  --blue:#5e8aa4;
  --olive:#a4a70f;
  --orange:#f9a21c;
  --sand:#dad2d0;
  --navy:#2f5f80;
  --ink:#333;
  --text:#555;
  --muted:#7a7a7a;
  --panel:#e6ebf0;
  --panel-light:#f0f1f3;
  --bg:#ececec;
}
*{box-sizing:border-box;margin:0;padding:0}
html,body{width:1086px;height:1200px;overflow:hidden;background:var(--bg)}
body{font-family:"Open Sans",sans-serif;color:var(--text)}
.sheet{position:absolute;left:80px;top:0;width:1451px;height:1880px;background:#fff;transform:scale(.6383);transform-origin:0 0;overflow:hidden}
.abs{position:absolute}
.display{font-family:"Passion One",sans-serif;color:var(--ink);letter-spacing:.5px}
.header{left:0;top:0;width:1451px;height:163px;background:linear-gradient(112deg,#e8f3df 0,#e8f3df 68%,#dfe6ee 68.1%,#dfe6ee 100%)}
.header h1{position:absolute;left:0;right:0;top:60px;text-align:center;font-size:58px;font-weight:700;line-height:1}
.hero-art{left:0;top:188px;width:690px;height:267px;background:linear-gradient(90deg,#5aa6c4 0%,#8cc3d8 45%,rgba(255,255,255,0) 100%)}
.intro{left:757px;top:256px;width:620px;font-size:21px;line-height:31px;color:var(--text)}
.lead{left:80px;top:478px;font-size:21px;color:var(--text)}
.lead b{color:var(--blue);font-size:25px;font-weight:600}
.panel{position:absolute;overflow:hidden}
.placeholder{position:absolute}
.tag{position:absolute;background:var(--navy);color:#fff;font-weight:700;text-align:center;clip-path:polygon(12% 0,88% 0,100% 100%,0 100%);line-height:1.05}
.tag-ring{position:absolute;border:3px solid var(--navy);border-radius:50%;border-bottom-color:transparent}
/* Panel A */
.pa{left:38px;top:529px;width:719px;height:414px;background:var(--panel)}
.pa .total{left:29px;top:58px;width:190px;font-size:20px;line-height:29px;color:var(--muted);font-weight:600}
.big{font-weight:600;color:var(--ink)}
.small-caps{font-size:.5em;font-weight:700}
.pa .dash{left:231px;top:39px;height:345px;border-left:2px dashed #555}
.pa .note{font-size:16px;line-height:23px;color:var(--muted)}
.pa .hl{color:var(--blue);font-weight:700}
/* Panel B */
.pb{left:785px;top:529px;width:628px;height:414px;background:var(--panel-light)}
.pb h2{position:absolute;left:0;right:0;top:20px;text-align:center;font-size:38px}
.col{position:absolute;top:69px;height:252px}
.col-head{height:43px;background:#a7b9c6;color:#2b2b2b;font-weight:700;font-size:15.5px;text-align:center;line-height:43px}
.col-body{height:127px}
.col-foot{height:82px;background:#f6f6f3}
.col .size{position:absolute;left:0;right:0;top:122px;text-align:center;font-weight:700;font-size:22px;color:#222}
.total-bar{left:55px;top:324px;width:502px;height:43px;background:var(--blue);color:#fff;font-weight:600;font-size:19px;text-align:center;line-height:43px}
.total-bar b{font-size:28px}
/* Panel C */
.pc{left:38px;top:971px;width:719px;height:617px;background:var(--panel-light)}
.pc h2{position:absolute;left:0;right:0;top:10px;text-align:center;font-size:52px}
.row{left:27px;top:69px;width:662px;height:113px;background:#dde3ea;overflow:hidden}
.row .lbl{font-size:20px;color:#333}
.row .val{font-size:33px;font-weight:600;color:#222}
.compare{left:24px;top:195px;width:673px;height:405px;background:#c8c8ca}
.cmp{position:absolute;top:14px;height:378px;text-align:center;color:#444}
.cmp .pct{font-family:"Open Sans",sans-serif;font-weight:600;font-size:27px;margin-top:28px}
.cmp .n{position:absolute;left:0;right:0;font-size:19px;font-weight:700}
.cmp .name{position:absolute;left:0;right:0;font-size:15px}
.cmp .box{position:absolute;height:32px;line-height:32px;color:#fff;font-size:25px;font-weight:600;background:#6d6d6d}
/* Panel D */
.pd{left:785px;top:968px;width:628px;height:437px;background:var(--panel-light)}
.pd h2{position:absolute;left:0;right:0;top:16px;text-align:center;font-size:26px}
.frame{position:absolute;background:#fff;border:3px solid var(--olive);box-shadow:-7px 7px 0 #cfd0d2}
.pd .num{font-size:27px;font-weight:600}
.pd .desc{font-size:16px;line-height:22px;color:#333}
.dashbox{position:absolute;border:2px dashed var(--blue);border-right:none}
.tiny{font-size:9.5px;line-height:13px;color:#333}
/* Panel E */
.pe{left:785px;top:1433px;width:628px;height:415px;background:var(--panel-light)}
.pe h2{position:absolute;left:0;right:0;top:18px;text-align:center;font-size:38px}
.pe .cap{font-size:16px;line-height:23px;color:#555}
.pe .cap b{color:var(--gold);font-weight:600}
.pe .aside{left:408px;top:92px;width:220px;height:321px;background:#dde3ea;padding:12px 16px 0 26px;font-size:17.5px;line-height:25.5px;color:#333}
.pe .aside b{color:var(--gold);font-weight:600}
.pe .foot{left:38px;top:358px;font-size:14px;font-style:italic;color:#555;line-height:20px}
.pe .foot span{color:var(--blue)}
/* Panel F */
.pf{left:38px;top:1616px;width:714px;height:232px;background:var(--panel-light)}
.pf .curve{left:0;top:0;width:700px;height:200px;background:var(--panel);border-radius:0 0 360px 0/0 0 200px 0}
.pf .k{font-size:15px;color:#333}
.pf .v{font-size:31px;font-weight:600;color:#222}
.clip{left:405px;top:6px;width:262px;height:236px;background:#fff;transform:rotate(-4deg);box-shadow:0 1px 4px rgba(0,0,0,.2);padding:12px 14px}
.clip .brand{font-weight:700;font-size:18px;color:#222;display:flex;align-items:center;gap:6px}
.clip .brand i{display:block;width:20px;height:20px;border-radius:50%;background:#222}
.clip .photo{margin-top:8px;height:92px;background:linear-gradient(180deg,#2f5d99,#6b8fb5 60%,#c9d3dc)}
.clip .head{margin-top:8px;font-family:"Libre Baskerville",serif;font-size:13px;line-height:16px;color:#111}
</style>
</head>
<body>
<div class="sheet">
  <div class="abs header"><h1 class="display">WILL POLYSTRENE BANS IMPROVE OCEAN HEALTH</h1></div>

  <div class="abs hero-art" role="img" aria-label="Illustration of a breaking ocean wave with floating plastic bottles and a school of fish"></div>
  <p class="abs intro">A recent report looks at the role plastics play in marine debris in the Great Pacific Garbage Patch (GPGP) that sheds light on previous assumptions about how different plastics contribute to the problem and where its coming from.</p>
  <p class="abs lead">Polystyrene ban legislation imply product restrictions will minimize plastic marine debris. <b>Let’s Take A Closer Look</b>.</p>

  <!-- Composition of GPGP mass -->
  <section class="panel pa">
    <p class="abs total">The total plastics mass in the GPGP is projected at<br><span class="big" style="font-size:33px;line-height:60px">78,908 <span class="small-caps">TONS</span></span></p>
    <div class="placeholder" role="img" aria-label="Illustration of a weighing scale" style="left:22px;top:199px;width:155px;height:155px;background:linear-gradient(180deg,#6d93ab,#557e97)"></div>
    <div class="abs dash"></div>
    <div class="placeholder" role="img" aria-label="Foam food tray icon" style="left:395px;top:2px;width:80px;height:42px;background:#dbe4eb"></div>
    <div class="abs big" style="left:407px;top:42px;font-size:28px">0.05%</div>
    <p class="abs note" style="left:493px;top:34px;width:210px">is <span class="hl">FOAMED PLASTICS</span> – including polystyrene – making it a minor component of the GPGP.</p>
    <svg class="abs" style="left:300px;top:98px" width="70" height="32"><polyline points="1,31 1,2 68,2" fill="none" stroke="#777" stroke-width="1.5"/></svg>
    <div class="abs big" style="left:261px;top:134px;font-size:40px">52%</div>
    <p class="abs note" style="left:265px;top:178px;width:130px">Mostly <span class="hl">ABANDONED FISHING GEAR</span>, not consumer plastics.</p>
    <div class="placeholder" role="img" aria-label="Icons of a fishing net, a fish and a fishing hook" style="left:255px;top:289px;width:137px;height:85px;background:#d3dde5"></div>
    <svg class="abs" style="left:366px;top:108px" width="180" height="180">
      <path d="M90,90 L90,8 A82,82 0 1 0 100,171.4 Z" fill="var(--blue)"/>
      <path d="M90,90 L90,23 A67,67 0 0 1 98.2,156.5 Z" fill="var(--gold)"/>
      <circle cx="90" cy="90" r="21" fill="#fff"/>
      <text x="14" y="84" fill="#fff" font-family="Open Sans" font-weight="700" font-size="24">52%</text>
      <text x="117" y="96" fill="#fff" font-family="Open Sans" font-weight="700" font-size="19">47%</text>
    </svg>
    <div class="placeholder" role="img" aria-label="Icons of rigid plastic pipes" style="left:542px;top:137px;width:140px;height:80px;background:#d3dde5"></div>
    <div class="abs big" style="left:543px;top:220px;font-size:40px">47%</div>
    <p class="abs note" style="left:496px;top:262px;width:215px">is <span class="hl">HARD PLASTICS</span>, <span class="hl">SHEETS</span> and <span class="hl">FILM</span>, making up the majority of the microplastics mass</p>
  </section>

  <!-- Sizing it up -->
  <section class="panel pb">
    <h2 class="display">SIZING IT UP</h2>
    <div class="col" style="left:20px;width:130px"><div class="col-head">MICROPLASTICS</div><div class="col-body" style="background:#efefef"></div><div class="col-foot"></div><div class="size">0.05-0.5cm</div></div>
    <div class="col" style="left:155px;width:127px"><div class="col-head">MESOPLASTICS</div><div class="col-body" style="background:#e9ecd9"></div><div class="col-foot"></div><div class="size">0.5-5cm</div></div>
    <div class="col" style="left:288px;width:150px"><div class="col-head">MACROPLASTICS</div><div class="col-body" style="background:#efefef"></div><div class="col-foot"></div><div class="size">5-50cm</div></div>
    <div class="col" style="left:444px;width:162px"><div class="col-head">MEGAPLASTICS</div><div class="col-body" style="background:#e9ecd9"></div><div class="col-foot"></div><div class="size">&gt;50cm</div></div>
    <div class="placeholder" style="left:78px;top:170px;width:14px;height:10px;background:#555"></div>
    <div class="placeholder" style="left:207px;top:165px;width:24px;height:16px;background:#a4a70f"></div>
    <div class="placeholder" style="left:345px;top:155px;width:40px;height:32px;background:#666"></div>
    <div class="placeholder" style="left:500px;top:128px;width:66px;height:58px;background:#7f851e"></div>
    <div class="tag-ring" style="left:77px;top:245px;width:16px;height:14px"></div><div class="tag" style="left:52px;top:255px;width:66px;height:48px;font-size:16px;padding-top:6px">6.5K<br>TONS</div>
    <div class="tag-ring" style="left:210px;top:245px;width:16px;height:14px"></div><div class="tag" style="left:185px;top:255px;width:66px;height:48px;font-size:16px;padding-top:6px">10K<br>TONS</div>
    <div class="tag-ring" style="left:355px;top:245px;width:16px;height:14px"></div><div class="tag" style="left:330px;top:255px;width:66px;height:48px;font-size:16px;padding-top:6px">20K<br>TONS</div>
    <div class="tag-ring" style="left:522px;top:245px;width:16px;height:14px"></div><div class="tag" style="left:497px;top:255px;width:66px;height:48px;font-size:16px;padding-top:6px">42K<br>TONS</div>
    <svg class="abs" style="left:0;top:303px" width="628" height="22"><g stroke="var(--navy)" stroke-width="3"><line x1="85" y1="0" x2="85" y2="21"/><line x1="218" y1="0" x2="218" y2="21"/><line x1="363" y1="0" x2="363" y2="21"/><line x1="530" y1="0" x2="530" y2="21"/></g></svg>
    <div class="abs total-bar">TOTAL GPGP &nbsp;<b>78,9K</b> <span style="font-size:14px">TONS</span></div>
  </section>

  <!-- How big is big -->
  <section class="panel pc">
    <h2 class="display">HOW BIG IS BIG?</h2>
    <div class="abs row">
      <div class="abs lbl" style="left:33px;top:24px">ALL GDP PLASTICS</div>
      <div class="abs val" style="left:30px;top:50px">78,908 <span class="small-caps" style="font-size:18px">TONS</span></div>
      <div class="tag-ring" style="left:238px;top:28px;width:16px;height:14px"></div><div class="tag" style="left:217px;top:38px;width:60px;height:50px;font-size:15px;padding-top:8px">50K<br>TONS</div>
      <div class="tag-ring" style="left:310px;top:28px;width:16px;height:14px"></div><div class="tag" style="left:289px;top:38px;width:60px;height:50px;font-size:15px;padding-top:8px">50K<br>TONS</div>
      <div class="abs" style="left:362px;top:0;width:300px;height:113px;background:#dde3ea"></div>
      <div class="abs" style="left:362px;top:22px;height:72px;border-left:2px solid var(--navy)"></div>
      <div class="abs lbl" style="left:391px;top:26px">All Foam Plastics</div>
      <div class="abs val" style="left:387px;top:50px">35 tons</div>
      <div class="tag" style="left:566px;top:38px;width:60px;height:50px;font-size:15px;padding-top:8px">50K<br>TONS</div>
    </div>
    <div class="abs compare">
      <div class="cmp" style="left:13px;width:187px;background:#dcd3d1">
        <div class="pct">GPGP = 79%</div>
        <div class="placeholder" role="img" aria-label="Illustration of a cruise ship" style="left:18px;top:128px;width:148px;height:70px;background:#b8b0ae"></div>
        <div class="n" style="top:204px">1</div><div class="name" style="top:232px">CRUISE SHIP</div>
        <div class="box" style="left:11px;width:163px;top:258px">100,000 <span style="font-size:15px">TONS</span></div>
        <div class="tag" style="left:28px;top:308px;width:58px;height:48px;font-size:14px;padding-top:8px">50K<br>TONS</div>
        <div class="tag" style="left:96px;top:308px;width:58px;height:48px;font-size:14px;padding-top:8px">50K<br>TONS</div>
      </div>
      <div class="cmp" style="left:200px;width:218px;background:#7b9eb5;color:#fff">
        <div class="pct">GPGP = 53%</div>
        <div class="placeholder" role="img" aria-label="Illustration of a blue whale" style="left:6px;top:108px;width:200px;height:75px;background:#4f7490"></div>
        <div class="n" style="top:194px;font-weight:400;font-size:22px">1</div><div class="name" style="top:222px;font-size:20px">BLUE WHALE</div>
        <div class="box" style="left:22px;width:180px;top:256px;background:#44687f">150,000 <span style="font-size:15px">TONS</span></div>
        <div class="tag" style="left:30px;top:312px;width:50px;height:44px;font-size:12px;padding-top:8px">50K<br>TONS</div>
        <div class="tag" style="left:86px;top:312px;width:50px;height:44px;font-size:12px;padding-top:8px">50K<br>TONS</div>
        <div class="tag" style="left:140px;top:312px;width:50px;height:44px;font-size:12px;padding-top:8px">50K<br>TONS</div>
      </div>
      <div class="cmp" style="left:418px;width:242px;background:#dcd3d1">
        <div class="pct">GPGP = 29%</div>
        <div class="placeholder" role="img" aria-label="Illustration of the New York City skyline with a garbage truck" style="left:13px;top:70px;width:229px;height:135px;background:linear-gradient(180deg,#cfc7c5,#8e8e8e)"></div>
        <div class="n" style="top:210px">1 WEEK</div><div class="name" style="top:234px">NYC WASTE GENERATION</div>
        <div class="box" style="left:38px;width:180px;top:258px">269,230 <span style="font-size:15px">TONS</span></div>
        <div class="tag" style="left:40px;top:305px;width:32px;height:28px;font-size:8px;padding-top:5px">50K<br>TONS</div>
        <div class="tag" style="left:78px;top:305px;width:32px;height:28px;font-size:8px;padding-top:5px">50K<br>TONS</div>
        <div class="tag" style="left:114px;top:305px;width:32px;height:28px;font-size:8px;padding-top:5px">50K<br>TONS</div>
        <div class="tag" style="left:150px;top:305px;width:32px;height:28px;font-size:8px;padding-top:5px">50K<br>TONS</div>
        <div class="tag" style="left:186px;top:305px;width:32px;height:28px;font-size:8px;padding-top:5px">50K<br>TONS</div>
        <div class="tag" style="left:34px;top:338px;width:16px;height:22px;font-size:7px;padding-top:4px">50<br>TO</div>
      </div>
    </div>
  </section>

  <!-- Mismanaged EPS -->
  <section class="panel pd">
    <h2 class="display">HOW MUCH MISMANAGED EPS WASTE WAS FOUND?</h2>
    <div class="frame" style="left:45px;top:62px;width:273px;height:340px">
      <div class="abs num" style="left:30px;top:18px;color:var(--olive)">320,000,000 <span style="font-size:12px">TONS</span></div>
      <p class="abs desc" style="left:30px;top:58px">Worldwide<br>Annual Plastics<br>Production</p>
      <div class="dashbox" style="left:28px;top:183px;width:110px;height:122px"></div>
      <div class="abs" style="left:40px;top:190px;color:var(--blue);font-weight:600;font-size:19px">78,908 <span style="font-size:9px">TONS</span></div>
      <div class="abs tiny" style="left:40px;top:214px">Total GPGP Plastics</div>
      <div class="abs" style="left:40px;top:234px;color:var(--blue);font-weight:600;font-size:15px">0.000024%</div>
      <div class="abs tiny" style="left:40px;top:256px">Percent of Global<br>Production in GPGP</div>
      <div class="placeholder" role="img" aria-label="Tall green bar showing worldwide plastics production" style="left:180px;top:110px;width:58px;height:166px;background:linear-gradient(90deg,#c8c46e,#d9d591)"></div>
    </div>
    <div class="frame" style="left:318px;top:77px;width:252px;height:301px;box-shadow:none">
      <div class="abs num" style="left:30px;top:14px;color:var(--brown)">6,620,000 <span style="font-size:12px">TONS</span></div>
      <p class="abs desc" style="left:30px;top:50px;font-size:15px;line-height:20px">Worldwide Expanded<br>Polystyrene (EPS)<br>Plastics Production</p>
      <div class="dashbox" style="left:30px;top:127px;width:110px;height:135px;border-color:var(--gold)"></div>
      <div class="abs" style="left:46px;top:138px;color:var(--gold);font-weight:600;font-size:18px">35 <span style="font-size:9px">TONS</span></div>
      <div class="abs tiny" style="left:46px;top:160px">Total GPGP<br><span style="color:var(--gold)">Foam Plastics</span></div>
      <div class="abs" style="left:46px;top:188px;width:90px;border-top:1px solid var(--gold)"></div>
      <div class="abs" style="left:46px;top:194px;color:var(--gold);font-weight:600;font-size:13px">0.0000053%</div>
      <div class="abs tiny" style="left:46px;top:220px">Percent of Global<br>Production in GPGP</div>
      <div class="placeholder" role="img" aria-label="Small cube showing foam plastics share" style="left:170px;top:132px;width:56px;height:106px;background:linear-gradient(180deg,#ddd2d0 70%,#bb8c09 70%)"></div>
    </div>
  </section>

  <!-- Surprising discoveries -->
  <section class="panel pe">
    <h2 class="display">SURPRISING DISCOVERIES</h2>
    <svg class="abs" style="left:110px;top:68px" width="180" height="180">
      <circle cx="88" cy="88" r="84" fill="#e2e2e2"/>
      <path d="M88,88 L4,88 A84,84 0 0 1 172,88 Z" fill="var(--olive)"/>
      <path d="M88,88 L172,88 A84,84 0 0 1 113.9,167.9 Z" fill="var(--orange)"/>
      <circle cx="88" cy="88" r="52" fill="#fff" fill-opacity=".22"/>
      <circle cx="88" cy="88" r="24" fill="#fff"/>
      <text x="52" y="44" fill="#fff" font-family="Open Sans" font-weight="700" font-size="27">50%</text>
      <text x="108" y="124" fill="#fff" font-family="Open Sans" font-weight="700" font-size="24">20%</text>
    </svg>
    <svg class="abs" style="left:88px;top:128px" width="220" height="130"><polyline points="20,118 20,2 32,2" fill="none" stroke="var(--olive)" stroke-width="2"/><polyline points="195,122 195,20 188,20" fill="none" stroke="var(--orange)" stroke-width="2"/></svg>
    <p class="abs cap" style="left:35px;top:224px;width:150px">Approximately 50% of GPGP Plastics are <b>From Marine-Based Sources.</b></p>
    <p class="abs cap" style="left:205px;top:258px;width:150px">20% of the GPGP Plastic Debris Is <b>From the 2011 Tohoku Tsunami</b></p>
    <p class="abs foot"><span>Beach Litter</span> Studies Were Not Indicative of<br>GPGP Content.</p>
    <div class="abs aside">All marine plastic debris is a problem! However, plastic product bans will be ineffective in reducing ocean debris, especially since the <b>U.S. contributes less than 1%</b> of the world's mismanaged plastic waste.</div>
  </section>

  <!-- Cars comparison -->
  <section class="panel pf">
    <div class="abs curve"></div>
    <div class="abs k" style="left:56px;top:26px">TOTAL GPGP MASS</div>
    <div class="abs v" style="left:50px;top:50px">&gt;43,000 <span style="font-size:26px">CARS</span></div>
    <div class="abs" style="left:54px;top:98px;width:276px;border-top:2px dashed #555"></div>
    <div class="abs k" style="left:50px;top:116px;font-size:18px">TOTAL FOAM PLASTIC MASS</div>
    <div class="abs v" style="left:50px;top:142px;font-size:28px">18 CARS</div>
    <div class="abs clip">
      <div class="brand"><i></i>COASTLINE REPORT</div>
      <div class="photo" role="img" aria-label="Photo of researchers on a sailboat hauling sampling nets at sea"></div>
      <p class="head">Great Pacific Garbage Patch weighs more than 43,000 cars and is much larger than we thought</p>
    </div>
  </section>
</div>
</body>
</html>
```